Lucky Orbit Fun Casino Entertainment

Looking to update my business card and make it look more modern, stand out and eye catching.
We are are fun casino business in Australia (primarily Sydney). Blackjack and Roulette are our most popular games although we have pretty much every game available for hire that you would find in a real casino. The final design would need to be sleek and appeal to the more upmarket corporate sector.
We mainly cater for Corporate Events, Private Parties, Fundraising Events, Team Building, Poker Tournaments
I think I'd prefer the colour Black.

Target Market(s)

High-end Corporate

Industry/Entity Type

Events

Contact Information for Business Card

Dale Hutchins
Director
1300 482 617
0431 758 209
info@luckyorbit.com.au
www.luckyorbit.com.au
Facebook & Instagram @luckyorbitshows (proper social icons preferred)

Colors
000000
0255a3

Requirements
Must have
• Front side:
• Logo
• Contact details
• 'Australia's #1 Fun Casino Specialists'
• Back:
• Logo
Nice to have
• Back:
• Corporate Events
• Private Parties
• Poker Tournaments
• Fundraising
• Props & Theming
• Photo Booth
• Horse Racing Events
• The Vegas Sign attached, maybe on the back of the card in the background...?

```html
<!DOCTYPE html>
<html lang="en">
<head>
<meta charset="utf-8">
<title>Lucky Orbit – Business Card</title>
<link rel="stylesheet" href="https://fonts.googleapis.com/css2?family=Montserrat:wght@700&family=Questrial&display=swap">
<style>
  :root {
    --stage: #1f1f1f;
    --card: #0a0a0a;
    --gold: #f5a623;
    --blue: #29a8e0;
    --white: #f2f2f2;
    --rule: #cfcfcf;
  }
  * { box-sizing: border-box; margin: 0; padding: 0; }
  html, body { width: 1200px; height: 1200px; overflow: hidden; background: var(--stage); }
  body { position: relative; font-family: "Questrial", sans-serif; color: var(--white); }

  .card {
    position: absolute; left: 110px; width: 980px; height: 540px;
    background: var(--card); overflow: hidden;
    box-shadow: 0 10px 30px rgba(0,0,0,.6);
  }
  .card--front { top: 40px; }
  .card--back { top: 620px; }

  /* front */
  .sign-photo {
    position: absolute; right: 0; top: 0; width: 620px; height: 540px;
    background:
      radial-gradient(ellipse 55% 60% at 65% 40%, rgba(255,214,140,.95) 0%, rgba(214,120,40,.75) 35%, rgba(140,30,20,.45) 60%, rgba(10,10,10,0) 85%);
  }
  .brand {
    position: absolute; display: flex; align-items: center; gap: 18px;
  }
  .brand__mark {
    border-radius: 50%; background: var(--gold); flex: none;
  }
  .brand__name {
    font-family: "Montserrat", sans-serif; font-weight: 700; color: var(--gold);
    letter-spacing: 1px; white-space: nowrap;
  }
  .card--front .brand { left: 250px; top: 150px; }
  .card--front .brand__mark { width: 110px; height: 110px; }
  .card--front .brand__name { font-size: 58px; }

  .services {
    position: absolute; left: 0; right: 0; top: 330px;
    text-align: center; font-size: 23px; letter-spacing: 1.2px; line-height: 1.55;
  }
  .services .sep { color: var(--gold); font-size: 18px; margin: 0 8px; }

  /* back */
  .person { position: absolute; left: 240px; top: 70px; }
  .person__name {
    font-family: "Montserrat", sans-serif; font-weight: 700; font-size: 30px;
    color: var(--gold); letter-spacing: 1px; text-transform: uppercase;
  }
  .person__role { font-size: 26px; color: var(--blue); letter-spacing: 1px; margin-top: -2px; }

  .contacts { position: absolute; left: 150px; top: 270px; list-style: none; }
  .contacts li {
    display: flex; align-items: center; gap: 14px;
    font-size: 26px; letter-spacing: 1.2px; height: 38px;
  }
  .contacts svg { width: 30px; height: 30px; flex: none; }

  .card--back .brand { right: 80px; top: 170px; }
  .card--back .brand__mark { width: 90px; height: 90px; }
  .card--back .brand__name { font-size: 40px; }

  .address {
    position: absolute; right: 80px; top: 330px; text-align: right;
    font-size: 24px; letter-spacing: 1.2px; line-height: 1.4;
  }

  .tagline {
    position: absolute; left: 20px; right: 20px; top: 470px;
    display: flex; align-items: center; gap: 18px; font-size: 27px; letter-spacing: 1px;
  }
  .tagline::before, .tagline::after { content: ""; flex: 1; height: 1px; background: var(--rule); }
  .tagline .gold { color: var(--gold); }
  .tagline .blue { color: var(--blue); }
</style>
</head>
<body>

<section class="card card--front">
  <div class="sign-photo" role="img" aria-label="Photograph of the Las Vegas welcome sign with glowing marquee lights"></div>
  <div class="brand">
    <span class="brand__mark"></span>
    <span class="brand__name">LUCKY ORBIT</span>
  </div>
  <p class="services">
    Corporate Events<span class="sep">♠</span>Private Parties<span class="sep">♠</span>Poker Tournaments<span class="sep">♠</span>Fundraising<br>
    Props &amp; Theming<span class="sep">♠</span>Photo Booth<span class="sep">♠</span>Horse Racing Events
  </p>
</section>

<section class="card card--back">
  <div class="person">
    <p class="person__name">Dale Hutchins</p>
    <p class="person__role">CEO/FOUNDER</p>
  </div>

  <ul class="contacts">
    <li>
      <svg viewBox="0 0 30 30" fill="none" stroke="var(--blue)" stroke-width="1.6"><circle cx="15" cy="15" r="13"/><path d="M11 8l3 4-2 2c1 2 3 4 5 5l2-2 4 3-2 3c-5 0-12-7-12-12z" fill="var(--blue)" stroke="none"/></svg>
      1300 482 617
    </li>
    <li>
      <svg viewBox="0 0 30 30" fill="none" stroke="var(--blue)" stroke-width="1.6"><circle cx="15" cy="15" r="13"/><rect x="11" y="7" width="8" height="5" fill="var(--blue)" stroke="none"/><rect x="8" y="12" width="14" height="7" rx="1" fill="var(--blue)" stroke="none"/><rect x="11" y="18" width="8" height="5" fill="var(--card)"/></svg>
      0431 758 209
    </li>
    <li>
      <svg viewBox="0 0 30 30" fill="none" stroke="var(--blue)" stroke-width="1.6"><circle cx="15" cy="15" r="13"/><rect x="8" y="10" width="14" height="10" fill="var(--blue)" stroke="none"/><path d="M8 10l7 6 7-6" stroke="var(--card)"/></svg>
      info@luckyorbit.com.au
    </li>
    <li>
      <svg viewBox="0 0 30 30" fill="none" stroke="var(--blue)" stroke-width="1.6"><circle cx="15" cy="15" r="13"/><circle cx="15" cy="15" r="7"/><ellipse cx="15" cy="15" rx="3" ry="7"/><path d="M8 15h14"/></svg>
      www.luckyorbit.com.au
    </li>
  </ul>

  <div class="brand">
    <span class="brand__mark"></span>
    <span class="brand__name">LUCKY ORBIT</span>
  </div>

  <p class="address">
    18 Harbour Lane<br>
    Level 4, Pyrmont<br>
    NSW 2009
  </p>

  <p class="tagline">
    <span><span class="gold">Australia's #1</span> <span class="blue">Fun Casino</span> Specialists</span>
  </p>
</section>

</body>
</html>
```